Maren's Treasured Tunes - 2014

I need a CD cover and insert design for a CD that includes songs my daughter (Maren Dulack) has recorded. She is a 17 year old vocalist and uses accompaniment tracks as well as 2 songs with live accompaniment. The CD is dedicated to her mother and each song is dedicated to an individual. The CD is intended to be given as gifts to family and friends.

The CD is titled "2014"

There are 5 songs on the CD:

1. "Evening Lantern" (originally recorded by Paolo Vantreni and Lorette Fave). This is a duet with Maren and her father.
2. "Open Road" (Originally recorded by Copper Hollows). This is a duet Maren and her father.
3. "All That Your Mercy Holds" (originally recorded by Gloria Bastrelli) This is sung by Maren. Accompanied on keyboard by Tamsin Holgreve.
4. "Keep a Light On For Me" (originally sung by Vera Castlewood).
5. "Lean On Us" (originally sung by Dario Quell) sung by Maren accompanied on guitar by Tamsin Holgreve.

This is a mixture of songs that have special meaning to Maren. The CD should convey her fun, bubbly but mature personality. It should be colorful and fun not dark and harsh. She is a "Texas" girl but she isn't into country music. She loves anything "Texas".

With the dedications included for each song and the CD, there will need to be interior printing and background design that may include a foldout in order to fit everything.

CD Dedication:
"I dedicate this cd to my mom. Even though I don't show it all the time, I appreciate her and the unconditional love she shows me. Through everything that I do I want to make her proud. Thank you for always having hope and faith in me and providing a life for me that I am so blessed to live. I love you more an more every day"

Song Dedications:
"Evening Lantern"
As many people know, “Evening Lantern” has been our most requested song to sing. Growing up I had heard my dad sing this song with my aunt and I was so mesmerized by their performances and couldn’t wait to one day sing this song with my dad. My dad and I have been singing together since I was 4 but this song sparked a different kind of relationship and musical connection with him. It was challenging at first and he pushed me to work hard and to push myself to discover vocal capabilities that I didn’t know I had. I dedicate this song to my dad for always motivating me to be the best I can be not only musically but socially, academically and most of all spiritually. Dad, I love you more than words can say.

"Open Road"
I have never been a fan of country music let alone attempted to sing a country song but this song completely changed my perspective on it. My dad and I first sang this song at our Pastors retirement party celebrating he and his wife’s 23 year long dedication to our church and to recognize his love for country music. They became apart of our family in many ways and I am so blessed to call them family. This song is dedicated to Pastor Glen and Faye Durbin for everything fron putting up with my grandparents to sharing every Easter with us. I miss them so much but I know that they will forever be apart of our family no matter where God places them.

"All That Your Mercy Holds"
When first introduced to this song I hated it. When having to choose a song to sing I always went with a ballad because that was my comfort zone. So when asked to sing a gospel song I was very overwhelmed. I never fully understood why people would say that they are “in love with music” or “music was their passion”. I obviously enjoyed music but I had never felt that connection with it until the first time I performed this song. Every note, every word, every dynamic meant something to me and my passion for music was forever changed. I dedicate this song to Tamsin Holgreve for working with me hour upon hour to help me vocally improve and for teaching me that it’s okay to step outside the box and to not just be comfortable all the time.

"Keep a Light on for Me"
I heard this song for the first time and sang it 3 days later for my end of the year choir concert. My mom had been searching songs for me to sing and as soon as she introduced this song to me I fell in love with it. This song is typically meant to be sung about a romantic love but while performing this song I couldn’t help but think of my grandparents and how they are always watching over me. I dedicate this song to my guardian angels, my protectors, and the two people that I love and miss more than anything in this world Oma and Opa.

"Lean On Us"
When I first sang this song I was performing at my voice recital for school. I chose to sing this song because it was fun and sweet. In the past few months this song has become very real to me. Although God and family are top priorities in my life, friends are such a huge part of my life as well. In 6Th grade I started a friendship with someone that I never knew would make such a great impact on my life. She became someone that I looked up to and someone that I could truly call my best friend. I dedicate this song to Kaylee Brandt for always putting up with me and investing in not only my life but my family’s life. No matter where life takes us in the next year I will forever be thankful for her friendship.

Special thanks to:

My Momma
Marla Quince (voice coach)
Lulu Padgett (High School choir director)
Mark Ostrand
Grant Vossler (Producer)

IMG_9670 is for the cover and IMG_9672 is for the back.

Thanks,

Curtis Dulack (father)

```html
<!DOCTYPE html>
<html lang="en">
<head>
<meta charset="utf-8">
<title>Maren's Treasured Tunes - 2014 — Song Dedications</title>
<link rel="stylesheet" href="https://fonts.googleapis.com/css2?family=EB+Garamond:ital,wght@0,400;0,700;1,400&display=swap">
<style>
  :root {
    --paper: #ffffff;
    --ink: #231f20;
    --trim: #a9dbe8;
  }
  * { box-sizing: border-box; margin: 0; padding: 0; }
  html, body {
    width: 1200px;
    height: 2690px;
    overflow: hidden;
    background: var(--paper);
  }
  body {
    position: relative;
    font-family: "EB Garamond", Garamond, serif;
    color: var(--ink);
    font-size: 32px;
    line-height: 43px;
  }
  .insert-panel {
    position: absolute;
    left: 2px;
    width: 1196px;
    border: 2px solid var(--trim);
  }
  .insert-panel--top { top: 0; height: 1310px; border-top: none; }
  .insert-panel--bottom { top: 1408px; height: 1256px; }
  .text-column {
    position: absolute;
    top: 26px;
    width: 550px;
  }
  .text-column--left { left: 38px; }
  .text-column--right { left: 608px; }
  .insert-panel--bottom .text-column { top: 8px; }
  .section-label {
    font-style: italic;
    margin-bottom: 12px;
  }
  .dedication { margin-bottom: 10px; }
  .song-title { font-weight: 700; }
  .thanks-label {
    font-style: italic;
    margin-top: 22px;
  }
  .thanks-list { list-style: none; }
  .thanks-name { font-weight: 700; }
</style>
</head>
<body>

<section class="insert-panel insert-panel--top">
  <div class="text-column text-column--left">
    <p class="section-label">Song Dedications:</p>
    <p class="dedication"><span class="song-title">Evening Lantern</span> This has been our most requested song to perform at weddings. When I was very young I heard my Dad sing this song with my Aunt and I was so mesmerized by their performance, I couldn’t wait to one day sing this song with my Dad. My Dad and I have been singing together since I was 4 years old but this song sparked a different kind of relationship and musical connection between us. It was challenging at first, but he inspired me to work hard and to push myself to discover vocal capabilities that I didn’t know I had. I dedicate this song to my Dad for always motivating me to do my best, not just musically but socially, academically and most of all spiritually. I love you more than words can say.</p>
    <p class="dedication"><span class="song-title">Open Road</span> I’ve never really appreciated country music let alone attempted to sing a country song but this song completely changed my perspective.</p>
  </div>
  <div class="text-column text-column--right">
    <p class="dedication">My Dad and I first sang this song at our Pastor’s retirement party celebrating him and his wife’s many years of service to our church and to recognize their love for country music. They became a part of our family in so many ways from sharing many holiday meals and special family events to their loving devotion to my grandparents and support for our family when my grandparents passed away. I am so blessed to call them family. This song is dedicated to Pastor Glen and Faye Durbin. I miss you so much but I know that you’ll forever be a part of our family.</p>
    <p class="dedication"><span class="song-title">All That Your Mercy Holds</span> When first introduced to this song I did not care for it. When choosing a song to perform at either church or an event, I normally went with a ballad because that was my comfort zone. When asked to sing a gospel song I was overwhelmed. I never fully understood why people would say that they were “in love with music” or “music was</p>
  </div>
</section>

<section class="insert-panel insert-panel--bottom">
  <div class="text-column text-column--left">
    <p class="dedication">their passion”. I obviously enjoyed music but I had never felt that connection with it until the first time I performed this song. Every note, every word, every dynamic of the song touched me and my passion for music was born. I dedicate this song to Tamsin Holgreve for working with me hour upon hour to help me improve vocally and for teaching me that it’s okay to step outside the box and my comfort zone.</p>
    <p class="dedication"><span class="song-title">Lean On Us</span> The first time that I sang this song was at my voice recital for school. I chose this song because it was fun and sweet. In the past few months this song has become very real to me. Although God and family are top priorities in my life, friends are such a huge part as well. In 6Th grade I began a friendship with someone that I never knew would make such an impact on my life. She became someone that I looked up to and that I could truly call my best friend. I dedicate this song to Kaylee Brandt for always</p>
  </div>
  <div class="text-column text-column--right">
    <p class="dedication">putting up with me and investing in not only my life but my family’s as well. No matter where life takes us in the next year I will forever be thankful for your friendship.</p>
    <p class="dedication"><span class="song-title">Keep a Light On For Me</span> I heard this song for the first time and sang it 3 days later for my end of the year choir concert. My mom had been searching songs for me to sing and as soon as she introduced this song to me I fell in love with it. This song is about a romantic love but while performing I couldn’t help but think of my Oma and Opa and how they are always watching over me. I dedicate this song to my guardian angels, my protectors, and the two people that I love and miss more than anything in this world.</p>
    <p class="thanks-label">Special thanks to:</p>
    <ul class="thanks-list">
      <li><span class="thanks-name">Owen Dulack</span> (brother)</li>
      <li><span class="thanks-name">Marla Quince</span> (voice coach)</li>
      <li><span class="thanks-name">Lulu Padgett</span> (choir director)</li>
      <li><span class="thanks-name">Mark Ostrand</span> (church stage director)</li>
      <li><span class="thanks-name">Grant Vossler</span> (Producer)</li>
    </ul>
  </div>
</section>

</body>
</html>
```